Consulting group
Business cards and stationary
Use same font as used in my logo
I think it is Swiss721?
Simple
Damon Fairley
President
417 W. Marlow Avenue, Apt 118 Ann Arbor, MI 48177
Damon@DamonFairley.com
www.TheCopperLantern.com
Looking for envelope, letterhead, and business card.
the logo? if you want to try putting a quote on it: "“The worst thing that can happen to a good cause is, not to be skillfully attacked, but to be ineptly defended.” - Corvelle. Not sure if I will like the quote on there or not.

```html
<!DOCTYPE html>
<html lang="en">
<head>
<meta charset="utf-8">
<title>The Copper Lantern — Stationery</title>
<link rel="stylesheet" href="https://fonts.googleapis.com/css2?family=Archivo:wght@400;700&display=swap">
<style>
  :root {
    --red: #e0141b;
    --ink: #1a1a1a;
    --grey: #6d6d6d;
    --paper: #ffffff;
    --backdrop: #d9dadc;
    --rule: #c9c9c9;
  }
  * { box-sizing: border-box; margin: 0; padding: 0; }
  html, body { width: 1200px; height: 862px; overflow: hidden; }
  body {
    background: var(--backdrop);
    font-family: "Archivo", "Helvetica Neue", Arial, sans-serif;
    color: var(--ink);
    position: relative;
  }
  .sheet {
    position: absolute;
    background: var(--paper);
    box-shadow: 0 2px 8px rgba(0,0,0,.18);
  }

  .brand { display: flex; align-items: flex-start; gap: 8px; }
  .brand-square { width: 22px; height: 22px; background: var(--red); flex: none; }
  .brand-name { font-weight: 700; font-size: 15px; line-height: 1.05; color: var(--ink); }
  .brand--light .brand-square { background: var(--paper); }
  .brand--light .brand-name { color: var(--paper); }
  .brand--large .brand-square { width: 34px; height: 34px; }
  .brand--large .brand-name { font-size: 21px; }

  .contact { font-size: 7.5px; line-height: 1.45; color: var(--grey); }
  .contact .accent { color: var(--red); }

  .letterhead { left: 40px; top: 40px; width: 380px; height: 537px; padding: 34px 36px; }
  .letterhead .contact { position: absolute; top: 36px; right: 36px; text-align: left; }
  .letter-body { margin-top: 52px; font-size: 8.5px; line-height: 1.65; color: #333; }
  .letter-body p { margin-bottom: 10px; }
  .signature {
    display: block; width: 110px; height: 32px; margin: 8px 0 4px;
    background: linear-gradient(90deg, #e4e4e4, #f3f3f3);
  }
  .signer { font-size: 8.5px; font-weight: 700; }
  .signer-title { font-size: 8px; color: var(--grey); }
  .letterhead .footer-rule { position: absolute; left: 36px; right: 36px; bottom: 28px; height: 3px; background: var(--red); }

  .fax { left: 450px; top: 40px; width: 300px; height: 424px; padding: 28px 28px; }
  .fax .contact { position: absolute; top: 30px; right: 28px; }
  .fax-title { margin-top: 40px; font-size: 22px; font-weight: 700; color: var(--red); }
  .fax-fields { margin-top: 18px; }
  .fax-field { display: flex; align-items: flex-end; gap: 8px; font-size: 9px; font-weight: 700; margin-bottom: 14px; }
  .fax-field span.line { flex: 1; border-bottom: 1px solid var(--rule); height: 10px; }
  .fax-notes { border-top: 2px solid var(--red); margin-top: 10px; height: 150px; }

  .card { width: 370px; height: 210px; left: 790px; border-radius: 6px; }
  .card-front { top: 40px; background: var(--red); padding: 30px 30px; }
  .card-quote-side { top: 500px; padding: 30px 30px; }
  .quote {
    position: absolute; left: 30px; right: 30px; bottom: 26px;
    font-size: 9.5px; line-height: 1.45;
  }
  .card-front .quote { color: var(--paper); }
  .card-quote-side .quote { color: var(--grey); }
  .quote-mark { font-weight: 700; font-size: 22px; line-height: 0; vertical-align: -8px; color: var(--paper); }
  .card-quote-side .quote-mark { color: var(--red); }
  .quote-source { display: block; margin-top: 3px; font-weight: 700; }

  .card-contact { top: 270px; display: flex; align-items: center; padding: 0 26px; }
  .card-contact .brand { width: 165px; }
  .card-divider { width: 1px; height: 130px; background: var(--rule); margin: 0 18px; }
  .person-name { font-size: 12px; font-weight: 700; color: var(--red); }
  .person-title { font-size: 8.5px; color: var(--grey); margin-bottom: 10px; }
  .card-contact .contact { font-size: 8.5px; }
  .contact-line { display: flex; align-items: center; gap: 5px; }
  .icon { width: 8px; height: 8px; flex: none; }

  .envelope { left: 40px; top: 610px; width: 700px; height: 222px; padding: 26px 30px; }
  .envelope .contact { margin-top: 10px; margin-left: 30px; }
</style>
</head>
<body>

  <section class="sheet letterhead">
    <div class="brand brand--large">
      <div class="brand-square"></div>
      <div class="brand-name">The<br>Copper<br>Lantern</div>
    </div>
    <div class="contact">
      417 W. Marlow Avenue, Apt 118<br>
      Alder Falls, OR 97177<br>
      <span class="accent">541.555.0142</span><br>
      Damon@DamonFairley.com<br>
      www.TheCopperLantern.com
    </div>
    <div class="letter-body">
      <p>Dear Client,</p>
      <p>Thank you for meeting with our team last week. We have reviewed your goals and prepared a short plan that outlines the first steps, the people involved and the timeline we expect to follow.</p>
      <p>Our approach is simple and direct. Each stage ends with a clear review so that you can judge the work before we move on, and every cost is agreed in writing first.</p>
      <p>Please call or write with any questions. We look forward to working with you.</p>
      <p>Sincerely,</p>
      <span class="signature" role="img" aria-label="Handwritten signature"></span>
      <div class="signer">Damon Fairley</div>
      <div class="signer-title">President</div>
    </div>
    <div class="footer-rule"></div>
  </section>

  <section class="sheet fax">
    <div class="brand">
      <div class="brand-square"></div>
      <div class="brand-name">The<br>Copper<br>Lantern</div>
    </div>
    <div class="contact">
      417 W. Marlow Avenue, Apt 118<br>
      Alder Falls, OR 97177<br>
      <span class="accent">541.555.0143</span>
    </div>
    <h1 class="fax-title">Fax Sheet</h1>
    <div class="fax-fields">
      <div class="fax-field">To:<span class="line"></span></div>
      <div class="fax-field">From:<span class="line"></span></div>
      <div class="fax-field">Date:<span class="line"></span></div>
      <div class="fax-field">Pages:<span class="line"></span></div>
    </div>
    <div class="fax-notes"></div>
  </section>

  <section class="sheet card card-front">
    <div class="brand brand--large brand--light">
      <div class="brand-square"></div>
      <div class="brand-name">The<br>Copper<br>Lantern</div>
    </div>
    <p class="quote">
      <span class="quote-mark">“</span>The worst thing that can happen to a good cause is, not to be skillfully attacked, but to be ineptly defended.<span class="quote-mark">”</span>
      <span class="quote-source">– Corvelle</span>
    </p>
  </section>

  <section class="sheet card card-contact">
    <div class="brand brand--large">
      <div class="brand-square"></div>
      <div class="brand-name">The<br>Copper<br>Lantern</div>
    </div>
    <div class="card-divider"></div>
    <div>
      <div class="person-name">Damon Fairley</div>
      <div class="person-title">President</div>
      <div class="contact">
        417 W. Marlow Avenue, Apt 118<br>
        Alder Falls, OR 97177<br>
        <div class="contact-line" style="margin-top:6px">
          <svg class="icon" viewBox="0 0 10 10"><path d="M2 1h2l1 2.5-1.3 1a6 6 0 0 0 2.8 2.8l1-1.3L10 6v2a1 1 0 0 1-1 1A8 8 0 0 1 1 2a1 1 0 0 1 1-1z" fill="#e0141b"/></svg>
          541.555.0142
        </div>
        <div class="contact-line">
          <svg class="icon" viewBox="0 0 10 10"><rect x="0.5" y="2" width="9" height="6" fill="none" stroke="#e0141b"/><path d="M.5 2l4.5 3.5L9.5 2" fill="none" stroke="#e0141b"/></svg>
          Damon@DamonFairley.com
        </div>
        <div class="contact-line">
          <svg class="icon" viewBox="0 0 10 10"><circle cx="5" cy="5" r="4.3" fill="none" stroke="#e0141b"/><path d="M.7 5h8.6M5 .7c-2.4 2.6-2.4 6 0 8.6M5 .7c2.4 2.6 2.4 6 0 8.6" fill="none" stroke="#e0141b" stroke-width=".8"/></svg>
          www.TheCopperLantern.com
        </div>
      </div>
    </div>
  </section>

  <section class="sheet card card-quote-side">
    <div class="brand brand--large">
      <div class="brand-square"></div>
      <div class="brand-name">The<br>Copper<br>Lantern</div>
    </div>
    <p class="quote">
      <span class="quote-mark">“</span>The worst thing that can happen to a good cause is, not to be skillfully attacked, but to be ineptly defended.<span class="quote-mark">”</span>
      <span class="quote-source">– Corvelle</span>
    </p>
  </section>

  <section class="sheet envelope">
    <div class="brand">
      <div class="brand-square"></div>
      <div class="brand-name">The<br>Copper<br>Lantern</div>
    </div>
    <div class="contact">
      417 W. Marlow Avenue, Apt 118<br>
      Alder Falls, OR 97177
    </div>
  </section>

</body>
</html>
```